Business Cards Design for the electrical wholesaler: clean bold dynamic :)

We need a business card design that would follow our latest brand guidelines. As an electrical wholesaler we want to bring a fresh look and feel into the industry. The design should be clean bold and dynamic. It should come alive with the renewed energy of our green colour. Our grey colour should keep things balanced and complement the notion of maturity and responsibility. We employ Lato as a corporate font however are not bound by this font and we’re open to interpretation here.

Target Market(s)

Electrical contractors

Industry/Entity Type

Business

Contact Information for Business Card

Logo
Name & Surname: Olena Dovbush
Job Title: Director of Marketing
Email: helen.dovbush@mailvane.example
Cell phone: XXX.XXX.XXXX
Address: 20917 - 87 Ave. Edmonton, AB, Canada. T6K 2R8
Business Phone: 780.555.0187
Website: www.qorvil.example

Font styles to use
Other font styles liked:
• Lato

Requirements
Must have
• Logo & website
Nice to have
• Brand elements - some of them you may find in the attached Brand Guidelines (e.g. three lines on the background signifying "W")

```html
<!DOCTYPE html>
<html lang="en">
<head>
<meta charset="utf-8">
<title>qorvil business cards</title>
<link href="https://fonts.googleapis.com/css2?family=Lato:wght@400;700&display=swap" rel="stylesheet">
<style>
  :root {
    --green: #8cc63f;
    --grey: #4b4b50;
    --text: #3a3a3d;
    --white: #ffffff;
    --bg-top: #2b2b2b;
    --bg-bottom: #060606;
  }
  * { margin: 0; padding: 0; box-sizing: border-box; }
  html, body { width: 1200px; height: 900px; overflow: hidden; }
  body {
    background: linear-gradient(180deg, var(--bg-top) 0%, #1a1a1a 55%, var(--bg-bottom) 100%);
    font-family: "Lato", Arial, sans-serif;
    position: relative;
  }
  .card {
    position: absolute;
    top: 300px;
    width: 442px;
    height: 272px;
    border-radius: 10px;
    overflow: hidden;
  }
  .card--front { left: 152px; background: var(--white); }
  .card--back { left: 622px; background: var(--green); }

  .brand {
    position: absolute;
    left: 0;
    right: 0;
    display: flex;
    flex-direction: column;
    align-items: center;
  }
  .brand__row { display: flex; align-items: center; gap: 12px; }
  .brand__name {
    font-weight: 700;
    color: var(--grey);
    line-height: 1;
    letter-spacing: -0.5px;
  }
  .brand__tagline {
    font-weight: 700;
    color: var(--grey);
    letter-spacing: 1.6px;
    text-transform: uppercase;
  }

  .card--front .brand { top: 32px; }
  .card--front .brand__mark { width: 34px; height: 34px; background: var(--green); }
  .card--front .brand__name { font-size: 50px; }
  .card--front .brand__tagline { font-size: 10px; margin-top: 6px; margin-left: 46px; }

  .card--back .brand { top: 96px; }
  .card--back .brand__mark { width: 40px; height: 40px; background: var(--white); }
  .card--back .brand__name { font-size: 60px; }
  .card--back .brand__tagline { font-size: 11px; margin-top: 8px; margin-left: 52px; }

  .person {
    position: absolute;
    right: 234px;
    top: 148px;
    text-align: right;
    white-space: nowrap;
  }
  .person__name { font-size: 19px; font-weight: 700; color: var(--text); line-height: 1.1; }
  .person__first { color: var(--green); }
  .person__title { font-size: 13px; color: var(--text); margin-top: 4px; }

  .contacts {
    position: absolute;
    left: 220px;
    top: 133px;
    list-style: none;
  }
  .contacts__item {
    display: flex;
    align-items: center;
    gap: 7px;
    font-size: 12.5px;
    color: var(--text);
    height: 19px;
    white-space: nowrap;
  }
  .contacts__icon { width: 9px; height: 9px; flex: none; }

  .address {
    position: absolute;
    left: 0;
    right: 0;
    top: 229px;
    text-align: center;
    font-size: 13.5px;
    color: var(--text);
    white-space: nowrap;
  }
</style>
</head>
<body>
  <section class="card card--front">
    <div class="brand">
      <div class="brand__row">
        <span class="brand__mark"></span>
        <span class="brand__name">qorvil</span>
      </div>
      <span class="brand__tagline">Electrical Wholesalers</span>
    </div>

    <div class="person">
      <p class="person__name"><span class="person__first">Olena</span> Dovbush</p>
      <p class="person__title">Director of Marketing</p>
    </div>

    <ul class="contacts">
      <li class="contacts__item">
        <svg class="contacts__icon" viewBox="0 0 10 10"><rect x="2.5" y="0.5" width="5" height="9" rx="1" fill="none" stroke="#8cc63f" stroke-width="1.2"/><rect x="4.3" y="7.3" width="1.4" height="1" fill="#8cc63f"/></svg>
        <span>780.555.0187</span>
      </li>
      <li class="contacts__item">
        <svg class="contacts__icon" viewBox="0 0 10 10"><path d="M1 4 Q5 0 9 4 L7.5 5 L6.5 3.8 L3.5 3.8 L2.5 5 Z" fill="#4b4b50"/><rect x="2.5" y="5.5" width="5" height="3.5" fill="#4b4b50"/></svg>
        <span>780.451.2311</span>
      </li>
      <li class="contacts__item">
        <svg class="contacts__icon" viewBox="0 0 10 10"><rect x="0.5" y="2" width="9" height="6.5" fill="#8cc63f"/><path d="M0.5 2 L5 5.5 L9.5 2" fill="none" stroke="#fff" stroke-width="0.9"/></svg>
        <span>helen.dovbush@mailvane.example</span>
      </li>
      <li class="contacts__item">
        <svg class="contacts__icon" viewBox="0 0 10 10"><path d="M4 6 L6 4 M3.2 4.6 L1.8 6 A1.7 1.7 0 0 0 4 8.2 L5.4 6.8 M6.8 5.4 L8.2 4 A1.7 1.7 0 0 0 6 1.8 L4.6 3.2" fill="none" stroke="#8cc63f" stroke-width="1.2" stroke-linecap="round"/></svg>
        <span>www.qorvil.example</span>
      </li>
    </ul>

    <p class="address">20917 - 87 Ave. Edmonton, AB, Canada. T6K 2R8</p>
  </section>

  <section class="card card--back">
    <div class="brand">
      <div class="brand__row">
        <span class="brand__mark"></span>
        <span class="brand__name">qorvil</span>
      </div>
      <span class="brand__tagline">Electrical Wholesalers</span>
    </div>
  </section>
</body>
</html>
```